Organizational health infographic

I work as an independent contractor with a larger consulting firm named "the Lantern Works" https://www.lanternworks-example.com/ I need a simple infographic that visually explains the 3 stages of our client engagement, and their respective steps and objectives. Im inclined to use a "subway" map system design (Ive included a a draft overview of the content (in PPT and a PDF) and b) a few sample subway style infographics. I

Target Market(s)

CEOs and Human Resources Officers

Font styles to use
Sans Serif

Colors

Designer to choose colors to be used in the design.

Requirements
Must have
• my contact info
• mark elwin 555-384-9021
• mark.elwin@lanternworksadvisory-example.com
• lantern works logo (I put it near the top center part of the page). Logo and book pictures can be found on the website https://www.lanternworks-example.com
Nice to have
• 1) the more consistent the font and colors are with the Lantern Works website, the better https://www.lanternworks-example.com
• 2) if its possible to have all 3 "subway lines" collapse into a single timeline, that would be cool.
• 3) If its possible to add a visual timeline that shows each stage taking approx 3 to 6 months, also cool.
• 4) in stage 3, Im not sure about whether to use the actual book pictures or simply the titles of each book at a "subway stop" circle.

```html
<!DOCTYPE html>
<html lang="en">
<head>
<meta charset="utf-8">
<title>Lantern Works – Engagement Stages</title>
<link href="https://fonts.googleapis.com/css2?family=Montserrat:wght@700;800&family=Roboto:wght@300;400;500;700&display=swap" rel="stylesheet">
<style>
  :root {
    --red: #e8212b;
    --green: #8cc63f;
    --blue: #29a9e0;
    --ink: #2b2f3a;
    --paper: #ffffff;
    --footer: #2a2f3a;
  }
  * { margin: 0; padding: 0; box-sizing: border-box; }
  html, body { width: 776px; height: 1200px; overflow: hidden; background: var(--paper); }
  body { font-family: "Roboto", Arial, sans-serif; color: var(--ink); }
  .sheet { position: relative; width: 776px; height: 1200px; overflow: hidden; }

  .brand { position: absolute; left: 44px; top: 62px; display: flex; align-items: center; gap: 12px; }
  .brand-dot { width: 46px; height: 46px; border-radius: 50%; background: var(--red); }
  .brand-name { font-size: 52px; font-weight: 500; color: var(--ink); letter-spacing: -1px; line-height: 1; }

  .contact { position: absolute; right: 41px; top: 64px; text-align: right; }
  .contact-name { font-size: 36px; line-height: 40px; }
  .contact-name b { font-weight: 700; }
  .contact-name span { font-weight: 300; }
  .contact-line { font-size: 14px; font-weight: 700; line-height: 15px; }
  .header-rule { position: absolute; left: 44px; top: 171px; width: 691px; height: 3px; background: var(--ink); }

  .map { position: absolute; left: 0; top: 0; }

  .stage-title { position: absolute; left: 245px; transform: translateX(-50%); font-family: "Montserrat", sans-serif; font-weight: 800; font-size: 23px; letter-spacing: 3px; }
  .stage-bar { position: absolute; left: 150px; width: 206px; height: 23px; color: #fff; font-size: 17px; text-align: center; line-height: 23px; }
  .bar-red { background: var(--red); }
  .bar-green { background: var(--green); }
  .bar-blue { background: var(--blue); }

  .stop { position: absolute; transform: translateX(-50%); text-align: center; font-size: 11px; line-height: 12px; white-space: nowrap; }
  .stop-main { font-weight: 700; font-size: 14px; line-height: 16px; }
  .pill { position: absolute; left: 165px; top: 538px; width: 173px; height: 18px; border-radius: 9px; background: var(--ink); color: #fff; font-size: 12px; text-align: center; line-height: 18px; }

  .objectives { position: absolute; left: 489px; width: 260px; }
  .obj-heading { font-family: "Montserrat", sans-serif; font-weight: 800; font-size: 18px; letter-spacing: 4px; margin-bottom: 4px; }
  .obj-group { font-size: 14px; font-weight: 700; margin-top: 5px; }
  .obj-list { list-style: none; font-size: 11px; line-height: 14px; }
  .obj-list li { position: relative; padding-left: 17px; }
  .obj-list li::before { content: ""; position: absolute; left: 9px; top: 5px; width: 3px; height: 3px; border-radius: 50%; background: var(--dot); }
  .obj-red { --dot: var(--red); }
  .obj-red .obj-heading { color: var(--red); }
  .obj-green { --dot: var(--green); }
  .obj-green .obj-heading { color: var(--green); }
  .obj-blue { --dot: var(--blue); }
  .obj-blue .obj-heading { color: var(--blue); }

  .footer { position: absolute; left: 0; top: 1082px; width: 776px; height: 118px; background: var(--footer); color: #fff; }
  .legend { position: absolute; left: 56px; top: 34px; display: flex; gap: 10px; }
  .legend-item { width: 52px; text-align: center; font-size: 8px; line-height: 10px; letter-spacing: 0.5px; }
  .legend-item svg { display: block; margin: 0 auto 6px; }
  .footer-divider { position: absolute; left: 322px; top: 26px; width: 2px; height: 72px; background: #fff; }
  .footer-url { position: absolute; left: 370px; top: 40px; font-size: 31px; font-weight: 500; }
</style>
</head>
<body>
<main class="sheet">
  <header>
    <div class="brand"><span class="brand-dot"></span><span class="brand-name">lantern works</span></div>
    <div class="contact">
      <div class="contact-name"><b>mark</b> <span>elwin</span></div>
      <div class="contact-line">555-384-9021</div>
      <div class="contact-line">mark.elwin@lanternworksadvisory-example.com</div>
    </div>
    <div class="header-rule"></div>
  </header>

  <svg class="map" width="776" height="1082" viewBox="0 0 776 1082" aria-hidden="true">
    <g fill="none" stroke="var(--ink)" stroke-width="3" stroke-dasharray="7 5">
      <path d="M80,353 V275 Q80,248 107,248 H412"/>
      <path d="M430,402 V468 Q430,490 408,490 H102 Q80,490 80,512 V608"/>
      <path d="M430,652 V760 Q430,780 410,780 H100 Q80,780 80,800 V913"/>
    </g>
    <g fill="none" stroke="var(--ink)" stroke-width="3">
      <path d="M80,376 H430"/>
      <path d="M96,614 L120,590 Q130,580 142,580 H400 Q430,580 430,605"/>
      <path d="M96,646 L120,675 Q128,685 142,685 H400 Q430,685 430,650"/>
      <path d="M96,919 L122,892 Q130,882 142,882 H400 Q430,882 430,912"/>
      <path d="M96,951 L122,985 Q130,995 142,995 H400 Q430,995 430,958"/>
    </g>
    <!-- stage 1 -->
    <g stroke="var(--red)" stroke-width="3">
      <circle cx="424" cy="250" r="12" fill="var(--red)"/>
      <circle cx="80" cy="376" r="23" fill="#fff"/>
      <circle cx="185" cy="376" r="12" fill="var(--red)"/>
      <circle cx="249" cy="376" r="12" fill="var(--red)"/>
      <circle cx="330" cy="376" r="20" fill="#fff"/>
      <polygon points="405,355 455,355 430,400" fill="#fff"/>
    </g>
    <!-- stage 2 -->
    <g stroke="var(--green)" stroke-width="3">
      <circle cx="80" cy="630" r="23" fill="#fff"/>
      <circle cx="166" cy="580" r="14" fill="#fff"/>
      <circle cx="250" cy="580" r="14" fill="#fff"/>
      <circle cx="336" cy="580" r="14" fill="#fff"/>
      <circle cx="166" cy="685" r="17" fill="#fff"/>
      <circle cx="224" cy="685" r="10" fill="var(--green)"/>
      <circle cx="281" cy="685" r="10" fill="var(--green)"/>
      <circle cx="338" cy="685" r="18" fill="#fff"/>
      <polygon points="405,605 455,605 430,650" fill="#fff"/>
    </g>
    <!-- stage 3 -->
    <g stroke="var(--blue)" stroke-width="3">
      <circle cx="80" cy="935" r="23" fill="#fff"/>
      <rect x="152" y="868" width="26" height="26" fill="#fff"/>
      <circle cx="225" cy="880" r="11" fill="#fff"/>
      <circle cx="271" cy="880" r="11" fill="#fff"/>
      <circle cx="317" cy="880" r="11" fill="#fff"/>
      <circle cx="363" cy="880" r="11" fill="#fff"/>
      <rect x="152" y="982" width="26" height="26" fill="#fff"/>
      <circle cx="355" cy="995" r="12" fill="#fff"/>
      <polygon points="405,912 455,912 430,958" fill="#fff"/>
    </g>
  </svg>

  <section class="stage stage-1">
    <div class="stage-title" style="top:220px">STAGE 1</div>
    <div class="stage-bar bar-red" style="top:248px">Excutive Launch</div>
    <div class="stop stop-main" style="left:80px;top:407px">2 Day</div>
    <div class="stop" style="left:187px;top:401px">Meeting<br>Audits</div>
    <div class="stop" style="left:249px;top:401px">Leader<br>Coaching</div>
    <div class="stop" style="left:330px;top:401px">Quarterly<br>Off Sites</div>
  </section>

  <section class="stage stage-2">
    <div class="stage-title" style="top:461px">STAGE 2</div>
    <div class="stage-bar bar-green" style="top:488px">Next Level Rollout</div>
    <div class="pill">Key leader conferences</div>
    <div class="stop stop-main" style="left:82px;top:661px">Key Leader<br>Kickoff</div>
    <div class="stop" style="left:224px;top:646px">Meeting<br>Audits</div>
    <div class="stop" style="left:281px;top:646px">Leader<br>Coaching</div>
    <div class="stop" style="left:166px;top:712px">Department<br>Team:Offsites</div>
    <div class="stop" style="left:338px;top:712px">Department<br>Rollouts</div>
  </section>

  <section class="stage stage-3">
    <div class="stage-title" style="top:752px">STAGE 3</div>
    <div class="stage-bar bar-blue" style="top:779px">Organizational Rollout</div>
    <div class="stop" style="left:225px;top:822px">The Five<br>Blind Spots<br>Of A Team</div>
    <div class="stop" style="left:317px;top:822px">The Truth<br>About Staff<br>Commitment</div>
    <div class="stop" style="left:165px;top:900px">Workshops</div>
    <div class="stop" style="left:271px;top:901px">The Steady<br>Team Player</div>
    <div class="stop" style="left:363px;top:901px">Lost<br>In Meetings</div>
    <div class="stop stop-main" style="left:76px;top:972px">Playbook<br>Rollout</div>
    <div class="stop" style="left:250px;top:979px">Train the trainers</div>
    <div class="stop" style="left:250px;top:999px">Train the leaders</div>
    <div class="stop" style="left:165px;top:1017px">Internal<br>Training</div>
    <div class="stop" style="left:357px;top:1017px">Closing The<br>Five Blind Spots<br>Of A Team</div>
  </section>

  <aside class="objectives obj-red" style="top:238px">
    <h2 class="obj-heading">OBJECTIVES</h2>
    <h3 class="obj-group">Team cohesion</h3>
    <ul class="obj-list"><li>Solid trust</li><li>Aligned expectations</li></ul>
    <h3 class="obj-group">Playbook 1.0</h3>
    <ul class="obj-list"><li>Aligned vision, values, strategy,<br>priorities &amp; roles</li></ul>
    <h3 class="obj-group">Productive meetings</h3>
    <ul class="obj-list"><li>Consistent communication with greater org</li></ul>
    <h3 class="obj-group">Transition readiness</h3>
    <ul class="obj-list"><li>Cohesion validation (CTAR)</li><li>Playbook Complete</li><li>Meeting Momentum</li></ul>
  </aside>

  <aside class="objectives obj-green" style="top:495px">
    <h2 class="obj-heading">OBJECTIVES</h2>
    <h3 class="obj-group">Key leaders</h3>
    <ul class="obj-list"><li>Finish Playbook 2.0</li><li>Become Ambassadors Of Org Health</li><li>Cross Functional Cooperation&nbsp; Playbook 2.0</li></ul>
    <h3 class="obj-group">Department teams</h3>
    <ul class="obj-list"><li>Cohesion, Clarity, Productive Meetings</li></ul>
    <h3 class="obj-group">Department rollouts</h3>
    <ul class="obj-list"><li>Break Down Silos</li><li>Dept Priorities&nbsp; Align To Org Priorities</li></ul>
    <h3 class="obj-group">Transition readiness</h3>
    <ul class="obj-list"><li>Ctars Department</li><li>Core Values Detailed And Implemented</li><li>Meeting Mastery</li></ul>
  </aside>

  <aside class="objectives obj-blue" style="top:783px">
    <h2 class="obj-heading">OBJECTIVES</h2>
    <h3 class="obj-group">All employees</h3>
    <ul class="obj-list"><li>Understand and utilize the playbook<br>Are equipped &amp; motivated to create a<br>healthy culture</li></ul>
    <h3 class="obj-group" style="margin-top:10px">Transition readiness</h3>
    <ul class="obj-list"><li>The consultation is completed when the<br>leaders are ready to assume responsibility<br>for maintaining a healthy culture.</li></ul>
  </aside>

  <footer class="footer">
    <div class="legend">
      <div class="legend-item"><svg width="30" height="30"><circle cx="15" cy="15" r="12" fill="none" stroke="#fff" stroke-width="3"/></svg>Live Off Site</div>
      <div class="legend-item"><svg width="30" height="30"><circle cx="15" cy="15" r="14" fill="#fff"/></svg>Video<br>Conference</div>
      <div class="legend-item"><svg width="30" height="30"><polygon points="3,4 27,4 15,26" fill="none" stroke="#fff" stroke-width="3"/></svg>Transition<br>Evaluation</div>
      <div class="legend-item"><svg width="30" height="30"><rect x="4" y="4" width="22" height="22" fill="none" stroke="#fff" stroke-width="3"/></svg>Training</div>
    </div>
    <div class="footer-divider"></div>
    <div class="footer-url">www.lanternworks-example.com</div>
  </footer>
</main>
</body>
</html>
```